5-star Hotel Web Design Project

I need a custom website design for a 5-star hotel. For full details please look at the attached ZIP archive.

The design should be in layers in Photoshop/Illustrator/InDesign format with all the icons/shapes/maps/graphic assets in vector format (svg, ai, eps) as much as possible.

I prefer white, simple but elegant websites. Please consider the performance/coding experience. We're not making something to show off our design skills on a design contest with fancy parallax effects and confusing animations. We're trying to create usable, functional and clean UI with good UX.

I would like to receive a few option for the color scheme to choose from.

The website will be custom coded, i.e. I'm not using WordPress.

NOTE: Don't bother to submit the generic WordPress style templates. We're looking for something custom made with attention to details. That's why the price is not guaranteed, but don't be mistaken, I'm a long time buyer here on FolioBazaar and all my projects are paid in full.
Updates

Low design quality

Target Market(s)

Europe

Industry/Entity Type

Hotel

Number of Pages Required

5+ page

```html
<!DOCTYPE html>
<html lang="en">
<head>
<meta charset="utf-8">
<title>Duskline Resort – Main Buffet Restaurants</title>
<link href="https://fonts.googleapis.com/css2?family=Montserrat:wght@400;500;600;700&display=swap" rel="stylesheet">
<style>
:root{
  --crimson:#a50d35;
  --gold:#d6b272;
  --gold-text:#d4a95c;
  --ink:#2b2b2b;
  --text:#555;
  --muted:#6a6a6a;
  --grey-bg:#f4f4f4;
  --line:#dcdcdc;
  --white:#fff;
}
*{box-sizing:border-box;margin:0;padding:0}
html,body{width:1200px;height:2942px;overflow:hidden}
body{font-family:'Montserrat',sans-serif;color:var(--text);background:var(--white);position:relative}

/* header */
.site-header{height:131px;position:relative}
.brand{position:absolute;left:100px;top:22px;width:180px;text-align:center;color:var(--crimson);white-space:nowrap}
.brand .mark{width:58px;height:58px;border-radius:50%;border:3px solid var(--crimson);margin:0 auto 8px}
.brand .name{font-size:21px;font-weight:500;line-height:1}
.contact-bar{position:absolute;right:112px;top:24px;font-size:17px;color:var(--ink);display:flex;align-items:center;gap:10px;white-space:nowrap}
.contact-bar svg{fill:var(--gold)}
.flag{width:26px;height:15px;background:#2a3f8f;display:inline-block;border:1px solid #c22}
.main-nav{position:absolute;right:112px;top:79px;display:flex;gap:35px;font-size:17px;font-weight:600;letter-spacing:.3px;color:var(--ink);white-space:nowrap}
.main-nav .active{color:var(--gold-text);font-weight:500}

/* hero gallery */
.hero{background:var(--grey-bg);height:907px;position:relative}
.hero h1{position:absolute;top:30px;width:100%;text-align:center;font-size:54px;font-weight:700;color:var(--ink);letter-spacing:.5px}
.hero .sub{position:absolute;top:107px;width:100%;text-align:center;font-size:16px}
.photo{position:absolute}
.p1{left:111px;top:165px;width:312px;height:315px;background:linear-gradient(160deg,#6b3a2e,#cbb9a4 60%,#8a5a4a)}
.p2{left:437px;top:165px;width:312px;height:315px;background:linear-gradient(160deg,#e8dcc0,#c9b88e 55%,#9aa7c6)}
.p3{left:763px;top:165px;width:312px;height:211px;background:linear-gradient(180deg,#f0ecea,#8aa0c0 55%,#9c7d5f)}
.p4{left:763px;top:390px;width:312px;height:211px;background:linear-gradient(180deg,#e9d9a7,#d5c9b4 55%,#7a5a3e)}
.p5{left:763px;top:614px;width:312px;height:211px;background:linear-gradient(180deg,#dfe6ee,#e8e1cf 50%,#8c8b86)}
.p6{left:111px;top:494px;width:638px;height:331px;background:linear-gradient(150deg,#c05a3a,#a9452e 50%,#e6ddd4 80%,#7a3a2a)}

/* restaurant details */
.details-intro{height:529px;position:relative}
.details-intro h2{position:absolute;left:111px;top:68px;font-size:34px;font-weight:600;color:var(--ink)}
.details-intro p{position:absolute;left:109px;top:130px;width:440px;font-size:16px;line-height:26.5px;color:var(--muted)}
.share-label{position:absolute;left:109px;top:316px;font-size:20px;font-weight:600;color:var(--ink)}
.socials{display:flex;gap:8px}
.socials span{width:43px;height:43px;border-radius:50%;border:1.5px solid var(--crimson);display:block}
.details-intro .socials{position:absolute;left:109px;top:360px}
.menu-card{position:absolute;left:596px;top:71px;width:488px;height:332px;border-radius:6px;overflow:hidden;background:var(--crimson);box-shadow:0 2px 6px rgba(0,0,0,.15)}
.menu-card .art{position:absolute;right:0;top:0;width:300px;height:332px;background:#dfad3d;border-radius:120px 0 0 0 / 330px 0 0 0;box-shadow:-8px 0 0 #3a2a26}
.menu-card h3{position:absolute;left:21px;top:84px;width:220px;color:var(--white);font-size:22px;font-weight:600;line-height:27px}
.btn{display:inline-flex;align-items:center;gap:6px;background:var(--gold);color:var(--white);font-weight:600;font-size:17px;padding:0 9px;height:53px;white-space:nowrap}
.btn svg{fill:var(--white)}
.menu-card .btn{position:absolute;left:21px;top:187px}

/* table section */
.details{background:var(--grey-bg);height:685px;position:relative}
.details h2{position:absolute;top:60px;width:100%;text-align:center;font-size:35px;font-weight:600;color:var(--ink)}
.details .sub{position:absolute;top:113px;width:100%;text-align:center;font-size:16px}
.venue-table{position:absolute;left:111px;top:178px;width:978px;border-collapse:separate;border-spacing:0;background:var(--white);border-radius:8px;overflow:hidden;box-shadow:0 0 0 1px var(--line);font-size:16px;color:var(--muted)}
.venue-table th{background:var(--crimson);color:var(--white);font-weight:600;font-size:18px;height:62px;border-right:1px solid rgba(255,255,255,.4)}
.venue-table th:last-child{border-right:0}
.venue-table td{text-align:center;border-right:1px solid #ccc;border-top:1px solid #ddd;line-height:23px;padding:0 4px}
.venue-table td:last-child{border-right:0}
.venue-table tr.single td{height:62px}
.venue-table tr.multi td{height:79px}
.venue-table td.meal{text-align:left;padding-left:9px}

/* all inclusive */
.program{height:273px;position:relative;background:linear-gradient(100deg,#3a2418,#6e4a34 35%,#5a3b2a 65%,#2e1c12);text-align:center;color:var(--white)}
.program h2{position:absolute;top:58px;width:100%;font-size:35px;font-weight:600}
.program p{position:absolute;top:120px;width:100%;font-size:16px}
.program .btn{position:absolute;left:483px;top:159px;height:52px}

/* footer */
.site-footer{height:417px;position:relative;color:var(--muted);font-size:16px}
.site-footer .brand{left:96px;top:30px}
.f-info{position:absolute;left:111px;top:172px;line-height:20px}
.f-info div{display:flex;gap:8px;margin-bottom:19px}
.f-info svg{fill:var(--gold);flex:none;margin-top:2px}
.f-col h4{font-size:21px;font-weight:600;color:var(--ink);margin-bottom:24px}
.f-col ul{list-style:none;line-height:35px}
.f-quick{position:absolute;left:457px;top:50px}
.f-quick .cols{display:flex;gap:26px}
.f-legal{position:absolute;left:842px;top:50px}
.f-rule{position:absolute;left:111px;top:317px;width:978px;border-top:1px solid var(--line)}
.copyright{position:absolute;left:111px;top:348px}
.site-footer .socials{position:absolute;right:111px;top:345px}
</style>
</head>
<body>

<header class="site-header">
  <div class="brand"><div class="mark"></div><div class="name">Duskline Resort</div></div>
  <div class="contact-bar">
    <svg width="14" height="14" viewBox="0 0 24 24"><path d="M6.6 10.8a15 15 0 0 0 6.6 6.6l2.2-2.2c.3-.3.7-.4 1-.2 1.1.4 2.3.6 3.6.6.6 0 1 .4 1 1V20c0 .6-.4 1-1 1A17 17 0 0 1 3 4c0-.6.4-1 1-1h3.5c.6 0 1 .4 1 1 0 1.3.2 2.5.6 3.6.1.3 0 .7-.2 1z"/></svg>
    <span>+359 500 200 47</span><span>|</span>
    <svg width="16" height="13" viewBox="0 0 24 18"><path d="M0 0h24v3L12 10 0 3zM0 5l12 7 12-7v13H0z"/></svg>
    <span>bookings@duskline-resort.example</span><span>|</span>
    <span class="flag"></span><span>English ▾</span>
  </div>
  <nav class="main-nav">
    <span class="active">DUSKLINE RESORT</span><span>BOOK DIRECT</span><span>SPECIAL OFFERS</span><span>LOCATION</span>
  </nav>
</header>

<section class="hero">
  <h1>MAIN BUFFET RESTAURANTS</h1>
  <div class="sub">Lumen, Ember house, Crystal, Azure, Verdant</div>
  <div class="photo p1" role="img" aria-label="Dining hall with chandeliers and set tables"></div>
  <div class="photo p2" role="img" aria-label="Buffet counter with salads and desserts"></div>
  <div class="photo p3" role="img" aria-label="Covered terrace with sea view"></div>
  <div class="photo p4" role="img" aria-label="Round restaurant hall under a domed ceiling"></div>
  <div class="photo p5" role="img" aria-label="Outdoor terrace with umbrellas in front of the hotel"></div>
  <div class="photo p6" role="img" aria-label="Restaurant with red walls and lattice screens"></div>
</section>

<section class="details-intro">
  <h2>RESTAURANTS DETAILS</h2>
  <p>Duskline Resort offers all types of meal supplement - bed and breakfast, half board (breakfast and dinner) and all inclusive (breakfast, lunch, dinner, all kinds of drinks - local alcoholic and non-alcoholic, soft and hot drinks, cocktails, afternoon coffee and cakes, ice cream).</p>
  <div class="share-label">Share:</div>
  <div class="socials"><span></span><span></span><span></span><span></span><span></span><span></span></div>
  <div class="menu-card">
    <div class="art" role="img" aria-label="Hand-drawn menu illustration with cutlery and kitchen tools"></div>
    <h3>Lorem ipsum dolor sit amet, consictet ur adipisci.</h3>
    <span class="btn"><svg width="15" height="17" viewBox="0 0 15 17"><path d="M1 0h9l5 5v12H1zM2 1v15h12V6H9V1z"/></svg>DOWNLOAD MENU</span>
  </div>
</section>

<section class="details">
  <h2>DETAILS</h2>
  <div class="sub">Each with its splendid sea view, One bedroom apartments offer a living space of 45-65 m².</div>
  <table class="venue-table">
    <colgroup><col style="width:206px"><col style="width:93px"><col style="width:139px"><col style="width:128px"><col style="width:231px"><col style="width:181px"></colgroup>
    <thead><tr><th>NAME*</th><th colspan="2">OPENING HOURS*</th><th>LOCATION</th><th>CAPACITY</th><th>SEASON</th></tr></thead>
    <tbody>
      <tr class="single"><td>Restaurant<br>“Ember house” (menu)</td><td colspan="2">18:00 – 21:00</td><td>Nord</td><td>hall – 130 seats and<br>terrace – 50 seats</td><td>June – September</td></tr>
      <tr class="multi"><td>Restaurant<br>“Lumen” (buffet)</td><td class="meal">breakfast<br>lunch<br>dinner</td><td>07:00 – 10:30<br>12:00 – 14:00<br>18:00 – 21:00</td><td>Nord</td><td>hall – 130 seats and<br>terrace – 50 seats</td><td>June – September</td></tr>
      <tr class="multi"><td>Restaurant<br>“Azure” (buffet)</td><td class="meal">breakfast<br>lunch<br>dinner</td><td>07:00 – 10:30<br>12:00 – 14:00<br>18:00 – 21:00</td><td>Nord</td><td>hall – 130 seats and<br>terrace – 50 seats</td><td>May – October</td></tr>
      <tr class="multi"><td>Restaurant<br>“Verdant” (buffet)</td><td class="meal">breakfast<br>lunch<br>dinner</td><td>07:00 – 10:30<br>12:00 – 14:00<br>18:00 – 21:00</td><td>Nord</td><td>hall – 130 seats and<br>terrace – 50 seats</td><td>May – October</td></tr>
      <tr class="multi"><td>Restaurant<br>“Crystal” (buffet)</td><td class="meal">breakfast<br>lunch<br>dinner</td><td>07:00 – 10:30<br>12:00 – 14:00<br>18:00 – 21:00</td><td>Nord</td><td>hall – 130 seats and<br>terrace – 50 seats</td><td>June – September</td></tr>
    </tbody>
  </table>
</section>

<section class="program" role="img" aria-label="Couple dining by candlelight in the restaurant">
  <h2>ALL-INCLUSIVE PROGRAM</h2>
  <p>Each with its splendid sea view, One bedroom apartments offer a living space of 45-65 m².</p>
  <span class="btn"><svg width="15" height="17" viewBox="0 0 15 17"><path d="M1 0h9l5 5v12H1zM2 1v15h12V6H9V1z"/></svg>DOWNLOAD MENU</span>
</section>

<footer class="site-footer">
  <div class="brand"><div class="mark"></div><div class="name">Duskline Resort</div></div>
  <div class="f-info">
    <div><svg width="11" height="15" viewBox="0 0 12 16"><path d="M6 0a6 6 0 0 1 6 6c0 4-6 10-6 10S0 10 0 6a6 6 0 0 1 6-6zm0 3.5a2.5 2.5 0 1 0 0 5 2.5 2.5 0 0 0 0-5z"/></svg><span>Duskline Resort, 48 Marina Vista<br>&nbsp;St. 8100 Seacliff, Bulgaria</span></div>
    <div><svg width="14" height="14" viewBox="0 0 24 24"><path d="M6.6 10.8a15 15 0 0 0 6.6 6.6l2.2-2.2c.3-.3.7-.4 1-.2 1.1.4 2.3.6 3.6.6.6 0 1 .4 1 1V20c0 .6-.4 1-1 1A17 17 0 0 1 3 4c0-.6.4-1 1-1h3.5c.6 0 1 .4 1 1 0 1.3.2 2.5.6 3.6.1.3 0 .7-.2 1z"/></svg><span>+359 500 200 47</span></div>
    <div><svg width="16" height="13" viewBox="0 0 24 18"><path d="M0 0h24v3L12 10 0 3zM0 5l12 7 12-7v13H0z"/></svg><span>bookings@duskline-resort.example</span></div>
  </div>
  <div class="f-col f-quick">
    <h4>Quick Links</h4>
    <div class="cols">
      <ul><li>Contact</li><li>Prices</li><li>Awards</li><li>Company details</li></ul>
      <ul><li>Hotel Fact Sheet</li><li>360® VR</li><li>Stay Safe Organizer</li><li>FAQ</li></ul>
    </div>
  </div>
  <div class="f-col f-legal">
    <h4>Legal</h4>
    <ul><li>Terms</li><li>Disclaimer</li><li>Privacy Policy</li></ul>
  </div>
  <div class="f-rule"></div>
  <div class="copyright">Copyright © 2021, Duskline Resort. All rights reserved.</div>
  <div class="socials"><span></span><span></span><span></span><span></span><span></span><span></span></div>
</footer>

</body>
</html>
```